Sportswear for local soccer teams Ad

Looking for a banner ad to be placed in a local soccer associations website. Brawlinmoor Logo must be shown. It should be short, eyecatching and want teams to visit or contact us about their kits or training apparel. Brawlinmoor is a doric word for delighted so any play on happiness, delight is fine. Size allowable is : 605x80. Also looking for a Skyscraper to be placed on all subsequent pages on their site. Size : 240x900

Target Market(s)

Football Teams

Industry/Entity Type

Sports Bar

```html
<!DOCTYPE html>
<html lang="en">
<head>
<meta charset="utf-8">
<title>Brawlinmoor Banner Ads</title>
<link rel="stylesheet" href="https://fonts.googleapis.com/css2?family=Arimo:wght@400;700&display=swap">
<style>
  :root {
    --canvas: #ffffff;
    --ink-black: #050505;
    --brand-orange: #f7941d;
    --text-white: #ffffff;
    --night-blue: #1b2a4a;
    --night-deep: #0a0f1c;
    --flood-light: #eef3ff;
    --cloud-orange: #d9782f;
    --sky-dusk: #3a2a22;
    --glow-warm: #fff1c9;
    --stand-brown: #5e4a36;
    --pitch-green: #4a7a2a;
    --pitch-dark: #17220e;
  }
  * { margin: 0; padding: 0; box-sizing: border-box; }
  html, body {
    width: 1200px; height: 900px; overflow: hidden;
    background: var(--canvas);
    font-family: "Arimo", Arial, sans-serif;
  }
  .canvas { position: relative; width: 1200px; height: 900px; }

  /* Leaderboard */
  .leaderboard {
    position: absolute; left: 81px; top: 436px;
    width: 606px; height: 81px;
    background: var(--ink-black); overflow: hidden;
  }
  .leaderboard .photo {
    position: absolute; left: 110px; top: 0; width: 496px; height: 81px;
    background:
      radial-gradient(ellipse 70px 40px at 230px 70px, var(--flood-light) 0%, rgba(150,175,230,0.55) 40%, rgba(27,42,74,0) 100%),
      radial-gradient(ellipse 60px 50px at 360px 40px, rgba(40,40,50,0.9) 0%, rgba(20,25,40,0) 100%),
      linear-gradient(90deg, var(--ink-black) 0%, var(--ink-black) 18%, var(--night-blue) 45%, var(--night-deep) 100%);
    clip-path: polygon(92px 0, 100% 0, 100% 100%, 80px 100%);
  }
  .leaderboard .brand {
    position: absolute; left: 22px; top: 16px; width: 82px;
    display: flex; flex-direction: column; align-items: center; gap: 5px;
  }
  .brand-dot {
    width: 32px; height: 32px; border-radius: 50%;
    border: 4px solid var(--brand-orange);
  }
  .brand-name {
    color: var(--brand-orange); font-weight: 700; letter-spacing: 0.3px;
    white-space: nowrap;
  }
  .leaderboard .brand-name { font-size: 12px; }
  .leaderboard .headline {
    position: absolute; left: 126px; top: 12px; width: 160px;
    color: var(--text-white); font-size: 17px; line-height: 22px;
    text-align: center; white-space: nowrap;
  }
  .shop-button {
    position: absolute; background: var(--brand-orange); color: var(--text-white);
    font-weight: 700; display: flex; align-items: center; justify-content: center;
    letter-spacing: 0.5px; white-space: nowrap;
  }
  .leaderboard .shop-button { left: 460px; top: 22px; width: 131px; height: 40px; font-size: 17px; }

  /* Skyscraper */
  .skyscraper {
    position: absolute; left: 742px; top: 100px;
    width: 194px; height: 729px;
    background: var(--ink-black); overflow: hidden;
  }
  .skyscraper .photo {
    position: absolute; left: 0; top: 213px; width: 194px; height: 516px;
    background:
      radial-gradient(ellipse 70px 45px at 95px 250px, var(--glow-warm) 0%, rgba(255,220,150,0.6) 35%, rgba(255,200,120,0) 100%),
      radial-gradient(ellipse 120px 70px at 40px 40px, rgba(217,120,47,0.9) 0%, rgba(217,120,47,0) 100%),
      radial-gradient(ellipse 90px 60px at 170px 150px, rgba(230,150,80,0.7) 0%, rgba(230,150,80,0) 100%),
      radial-gradient(ellipse 60px 110px at 150px 220px, rgba(235,235,240,0.55) 0%, rgba(235,235,240,0) 100%),
      linear-gradient(180deg, var(--sky-dusk) 0%, var(--cloud-orange) 22%, #9a6a4a 42%, var(--stand-brown) 55%, #3a3a26 60%, var(--pitch-green) 64%, #3b6622 80%, var(--pitch-dark) 100%);
    clip-path: polygon(0 27px, 100% 0, 100% 100%, 0 100%);
  }
  .skyscraper .brand {
    position: absolute; left: 0; top: 24px; width: 194px;
    display: flex; flex-direction: column; align-items: center; gap: 12px;
  }
  .skyscraper .brand-dot { width: 62px; height: 62px; border-width: 6px; }
  .skyscraper .brand-name { font-size: 22px; }
  .skyscraper .headline {
    position: absolute; left: 0; top: 135px; width: 194px;
    color: var(--brand-orange); font-weight: 700; font-size: 18px; line-height: 23px;
    text-align: center;
  }
  .skyscraper .shop-button { left: 15px; top: 632px; width: 164px; height: 43px; font-size: 24px; }
</style>
</head>
<body>
<div class="canvas">
  <section class="leaderboard">
    <div class="photo" role="img" aria-label="Footballer heading a ball under bright stadium floodlights"></div>
    <div class="brand">
      <span class="brand-dot"></span>
      <span class="brand-name">Brawlinmoor</span>
    </div>
    <p class="headline">Football Kits,<br>Training, Apparel<br>&amp; More</p>
    <div class="shop-button">SHOP NOW</div>
  </section>

  <section class="skyscraper">
    <div class="photo" role="img" aria-label="Footballer in white kit striking a ball on a floodlit pitch under a sunset sky"></div>
    <div class="brand">
      <span class="brand-dot"></span>
      <span class="brand-name">Brawlinmoor</span>
    </div>
    <p class="headline">Football Kits,<br>Training,<br>Apparel &amp; More</p>
    <div class="shop-button">SHOP NOW</div>
  </section>
</div>
</body>
</html>
```